Re-design my 1-page website to be BETTER!

Hi Guys,
I recently created a 1-page website for market testing purposes for a company I am starting. Problem is, the feedback i've had on the page is its a bit corporate and boring.
I would love you to design something that is fresher, more modern and will generate leads (via the sign up CTA's).
Here is the website as it is now: www.guidebridgehub.com.au.
If you need any info or have questions, just reach out.
Thanks,
Oliver

Target Market(s)

Entrepreneurs

Number of Pages Required

1 page

Font styles to use
Sans Serif

Colors
abd036
34a6d7
ffffff

Requirements
Must have
• Fresh, Modern, high-converting
• I expect 70% of traffic to be mobile so must be mobile optimised first.
Nice to have
• I've highlighted colours i like below, however, I am open to suggestions. I like colours that are gender neutral and show energy and vibrancy.
• I have used Proxima Nova for the fonts, as I find it easy to read however, I am open to suggestions. My main preference is that it displays well and is easily read

```html
<!DOCTYPE html>
<html lang="en">
<head>
<meta charset="utf-8">
<title>GuideBridge Hub – A Mentor For Everyone</title>
<link href="https://fonts.googleapis.com/css2?family=Montserrat:ital,wght@0,400;0,600;0,700;0,800;1,500&family=Open+Sans:wght@400;600;700&display=swap" rel="stylesheet">
<style>
:root{
  --green:#3ccf1c;
  --green-dark:#2fb012;
  --blue:#1637a3;
  --navy:#132d80;
  --ink:#333;
  --muted:#777;
  --grey-card:#e4e4e4;
  --grey-bg:#f6f6f6;
  --black:#0e0e0e;
  --white:#fff;
}
*{box-sizing:border-box;margin:0;padding:0}
html,body{width:1200px;height:3980px;overflow:hidden}
body{font-family:"Open Sans",Arial,sans-serif;color:var(--ink);background:var(--white);font-size:14px;line-height:1.6}
h1,h2,h3,h4,.btn,.nav a{font-family:"Montserrat",Arial,sans-serif}
.wrap{width:1060px;margin:0 auto;position:relative}

/* header */
.site-header{height:128px}
.site-header .wrap{display:flex;justify-content:space-between;align-items:center;height:128px}
.brand-name{font-family:"Montserrat",sans-serif;font-weight:700;font-size:30px;color:var(--navy);line-height:1}
.brand-tag{font-size:12px;color:var(--muted);margin-top:6px}
.header-meta{display:flex;align-items:center;gap:40px;font-size:15px;color:var(--navy);font-weight:600}
.phone{display:flex;align-items:center;gap:8px}
.follow{display:flex;align-items:center;gap:8px}
.follow span.sq{width:16px;height:16px;background:var(--navy);display:inline-block}

/* nav */
.nav{background:var(--green);height:36px}
.nav ul{list-style:none;display:flex;width:1060px;margin:0 auto;height:36px}
.nav li{flex:1;text-align:center}
.nav a{display:block;line-height:36px;color:var(--white);font-size:13px;font-weight:600;text-decoration:none}
.nav li.active a{background:var(--navy)}

/* hero */
.hero{position:relative;height:700px;background:linear-gradient(120deg,#5d6670 0%,#8d939a 45%,#b7b4ae 70%,#6f7478 100%);overflow:hidden}
.hero-copy{position:absolute;left:70px;top:150px;width:560px;color:var(--white)}
.hero-copy h1{font-size:64px;font-weight:700;line-height:1.05}
.hero-copy p{font-size:17px;margin-top:14px;line-height:1.45}
.hero-arrow{position:absolute;top:300px}
.hero-arrow.left{left:24px}.hero-arrow.right{right:24px}
.hero-curve{position:absolute;left:0;bottom:0;width:1200px;height:90px}

/* about */
.about{padding:60px 0 70px}
.about .wrap{display:flex;gap:60px}
.about-text{flex:1}
.section-title{font-size:34px;font-weight:700;color:var(--green)}
.title-rule{width:70px;height:3px;background:var(--green);margin:10px 0 30px}
.about-text h3{font-size:24px;font-weight:400;color:#555;font-family:"Open Sans",sans-serif;margin-bottom:18px}
.about-text p{font-size:13px;color:var(--muted);margin-bottom:14px}
.about-video{width:500px;height:290px;margin-top:40px;background:linear-gradient(135deg,#b6bcc2,#e3e3e0 60%,#9aa1a8);position:relative}
.about-video svg{position:absolute;left:50%;top:50%;transform:translate(-50%,-50%)}

/* steps */
.steps{background:var(--green);padding:60px 0 80px;height:740px}
.steps h2{text-align:center;color:var(--navy);font-size:36px;font-weight:700;margin-bottom:60px}
.step-row{display:flex;justify-content:space-between;width:1000px;margin:0 auto}
.step-card{width:290px;background:var(--white);padding:14px 14px 30px;text-align:center;height:430px}
.step-photo{height:200px;background:linear-gradient(135deg,#9fb0c4,#dfe5ec)}
.step-photo.p2{background:linear-gradient(135deg,#3d5e8c,#9db6d6)}
.step-photo.p3{background:linear-gradient(135deg,#c7c1b8,#efece6)}
.step-card h4{color:var(--navy);font-size:16px;margin:26px 0 12px}
.step-card p{font-size:13px;color:#555;line-height:1.5}

/* benefits */
.benefits{padding:70px 0;height:540px}
.benefits h2{text-align:center;color:var(--navy);font-size:40px;font-weight:800;letter-spacing:4px;line-height:1}
.benefits .sub{text-align:center;color:var(--blue);font-family:"Montserrat",sans-serif;font-style:italic;font-weight:500;font-size:26px;margin-top:6px}
.benefit-row{display:flex;justify-content:space-between;width:1060px;margin:40px auto 0}
.benefit-card{width:330px;background:var(--grey-card);border-radius:14px;padding:20px 30px 28px;text-align:center;height:290px;position:relative}
.benefit-icon{width:96px;height:96px;border-radius:50%;background:var(--navy);margin:0 auto;display:flex;align-items:center;justify-content:center}
.benefit-card h4{color:var(--navy);font-size:17px;margin:14px 0 8px}
.benefit-card p{font-size:12px;color:var(--muted);line-height:1.5}
.btn{display:inline-block;background:var(--green);color:var(--white);font-weight:700;font-size:12px;text-decoration:none;padding:9px 26px;border-radius:2px}
.benefit-card .btn{position:absolute;bottom:24px;left:50%;transform:translateX(-50%)}

/* stories */
.stories{background:var(--blue);padding:60px 0;height:640px}
.stories h2{text-align:center;color:var(--green);font-size:38px;font-weight:700;margin-bottom:60px}
.story-row{display:flex;justify-content:space-between;width:1060px;margin:0 auto}
.story{width:240px}
.story-bubble{background:var(--white);padding:70px 18px 22px;position:relative;height:290px}
.story-bubble::after{content:"";position:absolute;left:30px;bottom:-18px;border-left:18px solid transparent;border-right:0 solid transparent;border-top:18px solid var(--white)}
.avatar{position:absolute;top:-40px;left:50%;transform:translateX(-50%);width:86px;height:86px;border-radius:50%;border:4px solid var(--white);background:linear-gradient(135deg,#7c8fa6,#c4cdd8)}
.quote-mark{font-family:"Montserrat",sans-serif;font-size:40px;color:var(--navy);line-height:0.6;position:absolute;left:14px;top:70px}
.story-bubble p{font-size:12px;color:#555;line-height:1.5;padding-left:18px}
.story-name{text-align:right;color:var(--green);font-weight:600;font-size:14px;margin-top:26px}

/* faq */
.faq{padding:60px 0 40px;height:520px}
.faq h2{text-align:center;color:var(--navy);font-size:38px;font-weight:800}
.faq .title-rule{margin:8px auto 36px;background:var(--navy)}
.faq-cols{display:flex;justify-content:space-between}
.faq-col{width:510px}
.faq-item{border:2px solid var(--navy);height:38px;display:flex;align-items:center;justify-content:space-between;padding:0 16px;margin-bottom:14px;font-family:"Montserrat",sans-serif;font-weight:600;font-size:14px;color:var(--navy)}
.faq-item b{font-size:20px;font-weight:600}
.faq-open{background:var(--navy);padding:14px 16px 18px;margin-bottom:14px}
.faq-open h4{color:var(--white);font-size:14px;margin-bottom:14px}
.faq-open p{color:var(--green);font-size:12px;font-weight:700;line-height:1.5;margin-bottom:10px}
.faq-cta{text-align:center;margin-top:44px}
.faq-cta .btn{padding:10px 30px;font-size:13px}

/* cta band */
.cta-band{background:var(--blue);height:80px}
.cta-band .wrap{display:flex;align-items:center;justify-content:center;gap:80px;height:80px}
.cta-band h3{color:var(--white);font-size:26px;font-weight:800}
.cta-band .btn{padding:11px 40px;font-size:14px}

/* footer */
.site-footer{background:var(--black);color:#ccc;height:222px}
.footer-cols{display:flex;justify-content:space-between;padding-top:34px;height:186px}
.footer-col{width:320px}
.footer-col h4{color:var(--white);font-size:18px;font-weight:700;margin-bottom:8px}
.footer-col p{font-size:13px}
.socials{display:flex;gap:14px;margin-top:18px}
.socials span{width:18px;height:18px;border-radius:50%;background:#aaa}
.subscribe{display:flex;margin-top:20px}
.subscribe .field{flex:1;background:var(--white);height:34px;color:#999;font-size:12px;padding:8px 10px}
.subscribe .btn{border-radius:0;padding:10px 18px}
.copyright{border-top:1px solid #333;text-align:center;font-size:11px;color:#888;line-height:36px}
</style>
</head>
<body>

<header class="site-header">
  <div class="wrap">
    <div class="brand">
      <div class="brand-name">GuideBridge Hub</div>
      <div class="brand-tag">A Mentor For Everyone</div>
    </div>
    <div class="header-meta">
      <div class="phone">
        <svg width="16" height="16" viewBox="0 0 24 24"><path fill="#132d80" d="M6.6 10.8a15 15 0 0 0 6.6 6.6l2.2-2.2c.3-.3.7-.4 1-.2 1.1.4 2.3.6 3.6.6.6 0 1 .4 1 1V20c0 .6-.4 1-1 1A17 17 0 0 1 3 4c0-.6.4-1 1-1h3.5c.6 0 1 .4 1 1 0 1.3.2 2.5.6 3.6.1.3 0 .7-.2 1z"/></svg>
        (416) 555 0142
      </div>
      <div class="follow">Follow Us <span class="sq"></span><span class="sq"></span><span class="sq"></span><span class="sq"></span></div>
    </div>
  </div>
</header>

<nav class="nav">
  <ul>
    <li class="active"><a href="#">HOME</a></li>
    <li><a href="#">ABOUT US</a></li>
    <li><a href="#">SERVICES</a></li>
    <li><a href="#">HOW IT WORKS</a></li>
    <li><a href="#">NEWS</a></li>
    <li><a href="#">FAQS</a></li>
    <li><a href="#">CONTACT US</a></li>
  </ul>
</nav>

<section class="hero" role="img" aria-label="Photo of a smiling businesswoman in an office meeting room with colleagues behind her">
  <div class="hero-copy">
    <h1>GuideBridge Hub</h1>
    <p>Find the mentor who has walked your path. Practical guidance, honest feedback and real accountability to help your new business grow faster.</p>
  </div>
  <svg class="hero-arrow left" width="24" height="44" viewBox="0 0 24 44"><path d="M20 4 4 22l16 18" fill="none" stroke="#fff" stroke-width="3"/></svg>
  <svg class="hero-arrow right" width="24" height="44" viewBox="0 0 24 44"><path d="M4 4l16 18L4 40" fill="none" stroke="#fff" stroke-width="3"/></svg>
  <svg class="hero-curve" viewBox="0 0 1200 90" preserveAspectRatio="none">
    <path d="M0 90V40Q600 110 1200 20V90Z" fill="#fff"/>
    <path d="M0 40Q600 110 1200 20" fill="none" stroke="#3ccf1c" stroke-width="6"/>
  </svg>
</section>

<section class="about">
  <div class="wrap">
    <div class="about-text">
      <h2 class="section-title">ABOUT US</h2>
      <div class="title-rule"></div>
      <h3>Mentoring made simple for founders</h3>
      <p>We connect entrepreneurs with experienced business owners who have already faced the challenges you are facing now. Every mentor in our network is selected for real results, not just titles, and matched to your industry, stage and goals.</p>
      <p>Whether you are testing an idea, launching a product or scaling a team, your mentor gives you a trusted sounding board. Regular sessions keep you focused on what matters most and help you avoid costly mistakes along the way.</p>
      <p>Our mission is to make quality mentoring affordable and accessible for every founder, wherever they are.</p>
    </div>
    <div class="about-video" role="img" aria-label="Video still of a presenter speaking to a seated audience">
      <svg width="64" height="64" viewBox="0 0 64 64"><circle cx="32" cy="32" r="30" fill="#1637a3"/><path d="M26 20v24l18-12z" fill="#fff"/></svg>
    </div>
  </div>
</section>

<section class="steps">
  <h2>Mentorship but Different</h2>
  <div class="step-row">
    <article class="step-card">
      <div class="step-photo" role="img" aria-label="Photo of a person writing notes at a desk"></div>
      <h4>Tell Us What You Need</h4>
      <p>There is no one size fits all approach to mentorship. Tell us about your goals and the help you are looking for.</p>
    </article>
    <article class="step-card">
      <div class="step-photo p2" role="img" aria-label="Photo of a hand pointing to profiles on a digital screen"></div>
      <h4>Choose Your Mentor</h4>
      <p>Mentors are invited to our network. We match you with people who suit your needs, then you choose the one that fits.</p>
    </article>
    <article class="step-card">
      <div class="step-photo p3" role="img" aria-label="Photo of two people talking over coffee"></div>
      <h4>Ongoing Support</h4>
      <p>We don't stop once you have your mentor. We check in to make sure the pairing keeps delivering real progress.</p>
    </article>
  </div>
</section>

<section class="benefits">
  <h2>HOW A MENTOR</h2>
  <div class="sub">Will Accelerate Your Growth</div>
  <div class="benefit-row">
    <article class="benefit-card">
      <div class="benefit-icon"><svg width="44" height="44" viewBox="0 0 24 24"><path fill="#fff" d="M2 10h4v11H2zm6 11V10l5-8c1.5 0 2.5 1 2.2 2.6L14.5 9H20c1.2 0 2 1 1.8 2.2l-1.5 8A2 2 0 0 1 18.3 21z"/></svg></div>
      <h4>Clarity</h4>
      <p>A mentor helps you step back, see the bigger picture and decide where your time and money should go first.</p>
      <a class="btn" href="#">READ MORE</a>
    </article>
    <article class="benefit-card">
      <div class="benefit-icon"><svg width="44" height="44" viewBox="0 0 24 24"><path fill="#fff" d="M12 2l3 6.5 7 .8-5.2 4.8 1.4 7L12 17.6 5.8 21l1.4-7L2 9.3l7-.8z"/></svg></div>
      <h4>Motivation</h4>
      <p>Your mentor has been there before. Their belief and energy keep you going through the tough days.</p>
      <a class="btn" href="#">READ MORE</a>
    </article>
    <article class="benefit-card">
      <div class="benefit-icon"><svg width="44" height="44" viewBox="0 0 24 24"><path d="M4 12.5l5 5L20 6.5" fill="none" stroke="#fff" stroke-width="3"/></svg></div>
      <h4>Make you Accountable</h4>
      <p>A mentor holds you to the goals you set, so plans become actions and actions become results.</p>
      <a class="btn" href="#">READ MORE</a>
    </article>
  </div>
</section>

<section class="stories">
  <h2>Sucessful Stories</h2>
  <div class="story-row">
    <figure class="story">
      <div class="story-bubble">
        <div class="avatar" role="img" aria-label="Portrait photo of a client"></div>
        <span class="quote-mark">“</span>
        <p>My mentor helped me refine my pricing and land my first three clients within a month. I finally have a clear plan and someone in my corner who understands the journey.</p>
      </div>
      <figcaption class="story-name">Oliver</figcaption>
    </figure>
    <figure class="story">
      <div class="story-bubble">
        <div class="avatar" role="img" aria-label="Portrait photo of a client"></div>
        <span class="quote-mark">“</span>
        <p>Having a regular session kept me accountable. We tripled our online sales in six months and I learned more than any course could teach me about running a business.</p>
      </div>
      <figcaption class="story-name">Sarah</figcaption>
    </figure>
    <figure class="story">
      <div class="story-bubble">
        <div class="avatar" role="img" aria-label="Portrait photo of a client"></div>
        <span class="quote-mark">“</span>
        <p>I was stuck for a year before joining. My mentor asked the right questions and helped me rebuild my offer. The difference in confidence and revenue has been huge.</p>
      </div>
      <figcaption class="story-name">Daniel</figcaption>
    </figure>
    <figure class="story">
      <div class="story-bubble">
        <div class="avatar" role="img" aria-label="Portrait photo of a client"></div>
        <span class="quote-mark">“</span>
        <p>The matching process was quick and my mentor had built a business just like mine. Every meeting gives me practical steps I can put to work the same week.</p>
      </div>
      <figcaption class="story-name">Emma</figcaption>
    </figure>
  </div>
</section>

<section class="faq">
  <div class="wrap">
    <h2>FAQ'S</h2>
    <div class="title-rule"></div>
    <div class="faq-cols">
      <div class="faq-col">
        <div class="faq-item"><span>Q 1 &nbsp;WHAT IS A MENTOR?</span><b>+</b></div>
        <div class="faq-item"><span>Q 2 &nbsp;IS A MENTOR RIGHT FOR ME?</span><b>+</b></div>
        <div class="faq-item"><span>Q 3 &nbsp;HOW OFTEN DO WE MEET?</span><b>+</b></div>
        <div class="faq-item"><span>Q 4 &nbsp;CAN I HAVE MORE THAN ONE MENTOR?</span><b>+</b></div>
        <div class="faq-item"><span>Q 5 &nbsp;WHAT IF IT DOESN'T WORK OUT?</span><b>+</b></div>
      </div>
      <div class="faq-col">
        <div class="faq-open">
          <h4>Q 6 &nbsp;HOW DO WE MEET?</h4>
          <p>THE POWER OF MENTORING IS ONLINE. MEETINGS CAN BE HELD BY VIDEO CALL, PHONE OR IN PERSON, WHICHEVER SUITS YOU AND YOUR MENTOR BEST.</p>
          <p>WE FIND THAT FACE TO FACE MEETINGS ARE OFTEN NOT POSSIBLE, SO VIDEO CALLS ARE RECOMMENDED FOR FLEXIBILITY.</p>
        </div>
        <div class="faq-item"><span>Q 7 &nbsp;WHAT ARE THE COSTS?</span><b>+</b></div>
      </div>
    </div>
    <div class="faq-cta"><a class="btn" href="#">LEARN MORE</a></div>
  </div>
</section>

<section class="cta-band">
  <div class="wrap">
    <h3>ARE YOU READY FOR COACHING?</h3>
    <a class="btn" href="#">MAKE A APPOINTMENT</a>
  </div>
</section>

<footer class="site-footer">
  <div class="wrap footer-cols">
    <div class="footer-col">
      <h4>CONTACT ME</h4>
      <p>(416) 555 0142</p>
      <p>hello@guidebridgehub.com</p>
    </div>
    <div class="footer-col">
      <h4>CONNECT WITH US</h4>
      <p>Social Media Channels</p>
      <div class="socials"><span></span><span></span><span></span><span></span><span></span></div>
    </div>
    <div class="footer-col">
      <h4>NEWSLETTER</h4>
      <p>Signup for a special offers</p>
      <div class="subscribe"><div class="field">Email</div><a class="btn" href="#">SUBSCRIBE</a></div>
    </div>
  </div>
  <div class="copyright">Copyright © 2017 GuideBridge Hub | All Rights Reserved</div>
</footer>

</body>
</html>
```